VARNOLA SYSTEMS BUSINESS CARD DESIGN

WE WANT COMPLETE NEW DESIGN OF OUR BUSINESS CARD. WE ARE AN INTEGRATION COMPANY, WHERE WE INTEGRATE IOT/SMART SYSTEMS TO HOMES AND CORPORATE CUSTOMERS. WE SUPPLY AND INSTALL AUTOMATION PRODUCTS. THE FINAL DESIGN SHOULD COMMUNICATE TECHNOLOGY. THE CARD DESIGN SHOULD BE VERY IMPACT FULL. LOGO NEEDS TO BE THERE. IT WOULD NICE IF THE DESIGN WAS CLEAN. COLORS IS UP TO DESIGNER TO PLAY WITH, OR CAN STICK TO CORPORATE COLORS (FOLLOW LOGO). I HAVE ADDED FEW REFERENCE PHOTOS TO DRAW INSPIRATION MAYBE. I HAVE ADDED A HEX DESIGN, ITS NOT NECESSARY TO USE THIS DESIGN, ITS UPTO DESIGNER, JUST ADDED IF NEEDED TO PLAY WITH DESIGN.

Target Market(s)

Private end users and corporate clients

Industry/Entity Type

technology, home automation, home theaters, building management systems, IOT

Contact Information for Business Card

It should include Employee name, personal number, office number, email address, both in English and arabic. DETAILS TO INCLUDE :GERALD MOSSANE, MOBILE 0097150738915,OFFCIE 009714386207, GERALD@VARNOLAHUB.CO

Requirements
Must have
• Should feel like a technology company from design. Details both and in English and arabic (or at least have provision for arabic in design).
Nice to have
• I would like logo on one side, and details on the other side. Logo design side should communicate technology with logo. Other side can be clean just with information or also have some design aspects following from logo side. it would be interesting to see submissions with square design as well (that looks like an app Icon). colors could be of logo, red black grey and white. I have added some designs to draw inspiration from

```html
<!DOCTYPE html>
<html lang="en">
<head>
<meta charset="utf-8">
<title>Varnola Systems – Business Card</title>
<link rel="stylesheet" href="https://fonts.googleapis.com/css2?family=Arimo:wght@400;700&display=swap">
<style>
  :root {
    --backdrop: #141415;
    --card: #2e2e30;
    --card-edge: #262628;
    --red: #e3141b;
    --white: #f4f4f4;
    --grey: #b9b9bb;
    --rule: #cfcfd1;
  }
  * { margin: 0; padding: 0; box-sizing: border-box; }
  html, body { width: 1200px; height: 963px; overflow: hidden; }
  body {
    background: var(--backdrop);
    font-family: "Arimo", Arial, sans-serif;
    position: relative;
  }
  .business-card {
    position: absolute;
    left: 150px;
    top: 224px;
    width: 900px;
    height: 514px;
    background: linear-gradient(160deg, #323234 0%, var(--card) 55%, var(--card-edge) 100%);
    box-shadow: 0 20px 50px rgba(0,0,0,.6);
  }
  .contact-block {
    position: absolute;
    left: 58px;
    top: 268px;
  }
  .person-name {
    color: var(--red);
    font-weight: 700;
    font-size: 25px;
    letter-spacing: .3px;
  }
  .person-title {
    color: var(--white);
    font-size: 19px;
    margin-top: 6px;
  }
  .divider {
    position: absolute;
    left: 56px;
    right: 36px;
    top: 350px;
    height: 1.5px;
    background: var(--rule);
  }
  .contact-list {
    position: absolute;
    left: 58px;
    top: 368px;
    list-style: none;
  }
  .contact-item {
    display: flex;
    align-items: center;
    gap: 12px;
    color: var(--white);
    font-size: 19px;
    height: 30px;
  }
  .contact-item svg { width: 18px; height: 18px; flex: none; }
  .brand-lockup {
    position: absolute;
    right: 60px;
    top: 118px;
    text-align: right;
  }
  .brand-row {
    display: flex;
    align-items: center;
    justify-content: flex-end;
    gap: 18px;
  }
  .brand-dot {
    width: 52px;
    height: 52px;
    border-radius: 50%;
    background: var(--red);
    flex: none;
  }
  .brand-name {
    color: var(--white);
    font-weight: 700;
    font-size: 44px;
    letter-spacing: 1px;
    line-height: 1;
  }
  .brand-tagline {
    color: var(--white);
    font-size: 17px;
    letter-spacing: 5px;
    margin-top: 18px;
  }
</style>
</head>
<body>
  <article class="business-card">
    <div class="brand-lockup">
      <div class="brand-row">
        <span class="brand-dot"></span>
        <span class="brand-name">VARNOLA SYSTEMS L.L.C</span>
      </div>
      <p class="brand-tagline">A VARNOLA GROUP DIVISION.</p>
    </div>

    <div class="contact-block">
      <h1 class="person-name">GERALD MOSSANE</h1>
      <p class="person-title">General Manager</p>
    </div>

    <div class="divider"></div>

    <ul class="contact-list">
      <li class="contact-item">
        <svg viewBox="0 0 18 18" aria-hidden="true"><rect x="5" y="1.5" width="8" height="15" rx="1.5" fill="none" stroke="#e3141b" stroke-width="1.6"/><line x1="8" y1="14" x2="10" y2="14" stroke="#e3141b" stroke-width="1.4"/></svg>
        <span>0097150738915</span>
      </li>
      <li class="contact-item">
        <svg viewBox="0 0 18 18" aria-hidden="true"><path d="M4 2l3 3-1.5 2.2c1 2 2.3 3.3 4.3 4.3L12 10l3 3-2 2.5C7.5 15 3 10.5 2.5 4.5z" fill="#e3141b"/></svg>
        <span>009714386207</span>
      </li>
      <li class="contact-item">
        <svg viewBox="0 0 18 18" aria-hidden="true"><rect x="1.5" y="4" width="15" height="10" fill="none" stroke="#e3141b" stroke-width="1.5"/><path d="M1.5 4l7.5 6 7.5-6" fill="none" stroke="#e3141b" stroke-width="1.5"/></svg>
        <span>GERALD@VARNOLAHUB.CO</span>
      </li>
    </ul>
  </article>
</body>
</html>
```